Specialised investor in e-mobility and energy wants business card design

We need a business card design that fits our existing corporate design. <The look and feel must be 'sharp'/'clean', dynamic, communicate momentum, professionalism etc (as one would imagine from a firm in the financial sector). We like the idea of a reverse-side of the card that includes the logo, and the name and contact details on the other. We expect the deliverable to be whatever format might be required to be able to get cards printed directly by a service such as marlo cards. Our website is www.obrel.finance

```html
<!DOCTYPE html>
<html lang="en">
<head>
<meta charset="utf-8">
<title>Obrel Finance – Business Card</title>
<link rel="stylesheet" href="https://fonts.googleapis.com/css2?family=Montserrat:wght@400;500;700&display=swap">
<style>
  :root {
    --stage: #3a3a3a;
    --leaf: #8ab34c;
    --forest: #2f4d1f;
    --paper: #ffffff;
    --ink: #1e2a16;
    --accent: #8ab34c;
  }
  * { box-sizing: border-box; margin: 0; padding: 0; }
  html, body { width: 1200px; height: 689px; overflow: hidden; }
  body {
    background: var(--stage);
    font-family: "Montserrat", sans-serif;
    position: relative;
  }
  .card {
    position: absolute;
    top: 190px;
    width: 540px;
    height: 309px;
    overflow: hidden;
  }
  .card--front { left: 40px; background: var(--leaf); }
  .card--back { left: 620px; background: var(--paper); }

  .brand {
    position: absolute;
    display: flex;
    align-items: center;
    gap: 12px;
    color: var(--forest);
    font-weight: 500;
    white-space: nowrap;
  }
  .brand__dot {
    width: 14px; height: 14px; border-radius: 50%;
    background: var(--forest);
  }
  .card--front .brand { left: 0; right: 0; top: 128px; justify-content: center; font-size: 44px; }
  .card--front .brand__dot { width: 20px; height: 20px; }
  .card--back .brand { left: 34px; top: 112px; font-size: 27px; }

  .divider {
    position: absolute;
    left: 292px; top: 52px;
    width: 1.5px; height: 130px;
    background: var(--accent);
  }
  .contact {
    position: absolute;
    left: 308px; top: 50px;
    color: var(--ink);
    font-size: 12.5px;
    line-height: 17px;
  }
  .contact__name {
    color: var(--accent);
    font-weight: 700;
    font-size: 13.5px;
    letter-spacing: 0.02em;
  }
  .contact__line { display: flex; align-items: center; gap: 6px; }
  .contact__icon { width: 10px; height: 10px; flex: none; }
  .wave { position: absolute; left: 0; bottom: 0; width: 540px; height: 160px; }
</style>
</head>
<body>
  <section class="card card--front" aria-label="Card front">
    <div class="brand"><span class="brand__dot"></span>Obrel Finance</div>
  </section>

  <section class="card card--back" aria-label="Card back">
    <div class="brand"><span class="brand__dot"></span>Obrel Finance</div>
    <div class="divider"></div>
    <div class="contact">
      <p class="contact__name">ELIAS BRANDT</p>
      <p>team directly</p>
      <p>Obrel Finance S.A.</p>
      <p>Geneva, Switzerland</p>
      <p class="contact__line">
        <svg class="contact__icon" viewBox="0 0 10 10"><path d="M2 1h2l1 2-1.2 1a5 5 0 0 0 2.2 2.2L7 5l2 1v2a1 1 0 0 1-1 1A8 8 0 0 1 1 2a1 1 0 0 1 1-1z" fill="var(--accent)"/></svg>
        +41 79555 0142</p>
      <p class="contact__line">
        <svg class="contact__icon" viewBox="0 0 10 10"><rect x="0.5" y="2" width="9" height="6.5" fill="var(--accent)"/><path d="M0.5 2l4.5 3.5L9.5 2" stroke="#fff" stroke-width="0.9" fill="none"/></svg>
        elias@obrel.finance</p>
      <p class="contact__line">
        <svg class="contact__icon" viewBox="0 0 10 10"><circle cx="5" cy="5" r="4.5" fill="var(--accent)"/><path d="M0.5 5h9M5 0.5c-2.4 2.6-2.4 6.4 0 9M5 0.5c2.4 2.6 2.4 6.4 0 9" stroke="#fff" stroke-width="0.7" fill="none"/></svg>
        www.obrel.finance</p>
    </div>
    <svg class="wave" viewBox="0 0 540 160" preserveAspectRatio="none" aria-hidden="true">
      <path d="M0 150 C 160 150, 260 120, 360 70 S 500 10, 540 8 L540 160 L0 160 Z" fill="var(--forest)"/>
      <path d="M0 154 C 170 152, 270 126, 370 78 S 505 20, 540 18 L540 160 L0 160 Z" fill="var(--paper)"/>
      <path d="M0 160 C 180 156, 280 132, 380 86 S 510 26, 540 24 L540 160 Z" fill="var(--leaf)"/>
    </svg>
  </section>
</body>
</html>
```